need to update our new address on letterhead and business cards. Also open to
a redesign and logo in the near future as we are changing our name. New address is Bramcote Commerce Court, 781 Ashgrove Street, Ashford Vale, CT 06287

Target Market(s)

35-75 yrs of age

Industry/Entity Type

Business

Requirements
Nice to have
• We are a financial firm so this need to look impressive and classy

```html
<!DOCTYPE html>
<html lang="en">
<head>
<meta charset="utf-8">
<title>Harborline Financial Letterhead</title>
<link rel="stylesheet" href="https://fonts.googleapis.com/css2?family=Open+Sans:wght@400;600&display=swap">
<style>
  :root {
    --navy: #1b2a55;
    --ink: #3a3a3a;
    --rule: #8a8a8a;
    --paper: #ffffff;
    --backdrop: #e9e9e9;
  }
  * { margin: 0; padding: 0; box-sizing: border-box; }
  html, body {
    width: 1066px; height: 1200px; overflow: hidden;
    background: var(--backdrop);
  }
  .letterhead {
    position: relative;
    width: 1066px; height: 1200px;
    background: var(--paper);
    font-family: "Open Sans", Arial, sans-serif;
    color: var(--ink);
  }
  .header {
    position: absolute; top: 62px; left: 70px; right: 60px;
    display: flex; align-items: flex-start;
  }
  .brand-name {
    width: 440px; flex: none;
    font-size: 34px; font-weight: 400; color: var(--navy);
    line-height: 1; margin-top: 10px;
  }
  .address {
    font-style: normal; font-size: 12px; line-height: 16px;
    padding-right: 12px; margin-left: auto;
    border-right: 1.5px solid var(--ink);
  }
  .contact {
    list-style: none; font-size: 12px; line-height: 16px; padding-left: 10px;
  }
  .contact li { display: flex; align-items: center; gap: 6px; white-space: nowrap; }
  .contact svg { width: 9px; height: 9px; flex: none; }
  .footer {
    position: absolute; left: 0; right: 0; bottom: 0;
  }
  .footer-rule {
    margin: 0 50px; border-top: 1px solid var(--rule);
  }
  .disclaimer {
    text-align: center; font-size: 11.5px; line-height: 14px;
    padding: 6px 30px 10px; color: var(--ink);
  }
  .base-band { height: 10px; background: var(--navy); }
</style>
</head>
<body>
<main class="letterhead">
  <header class="header">
    <div class="brand-name">Harborline Financial</div>
    <address class="address">
      Bramcote Commerce Court<br>
      781 Ashgrove Street<br>
      Ashford Vale, CT 06287
    </address>
    <ul class="contact">
      <li><svg viewBox="0 0 10 10"><circle cx="5" cy="5" r="5" fill="#1b2a55"/><path d="M3 2.5 L4 2.5 L4.5 3.8 L3.9 4.3 Q4.6 5.6 5.7 6.1 L6.2 5.5 L7.5 6 L7.5 7 Q4 7.3 3 2.5Z" fill="#fff"/></svg>203-555-0148</li>
      <li><svg viewBox="0 0 10 10"><circle cx="5" cy="5" r="5" fill="#1b2a55"/><rect x="2.6" y="4" width="4.8" height="3" fill="#fff"/><rect x="3.5" y="2.5" width="3" height="1.5" fill="#fff"/></svg>203-555-0162</li>
      <li><svg viewBox="0 0 10 10"><circle cx="5" cy="5" r="5" fill="#1b2a55"/><rect x="2.5" y="3.3" width="5" height="3.4" fill="#fff"/><path d="M2.5 3.3 L5 5.2 L7.5 3.3" stroke="#1b2a55" stroke-width="0.6" fill="none"/></svg>RAldana@HarborlineFinancialSvcs.com</li>
      <li><svg viewBox="0 0 10 10"><circle cx="5" cy="5" r="5" fill="#1b2a55"/><circle cx="5" cy="5" r="2.6" stroke="#fff" stroke-width="0.7" fill="none"/><path d="M2.4 5 H7.6 M5 2.4 V7.6" stroke="#fff" stroke-width="0.6"/></svg>www.harborlinefinancialsvcs.com</li>
    </ul>
  </header>

  <footer class="footer">
    <div class="footer-rule"></div>
    <p class="disclaimer">
      Securities offered through Norwell Financial Specialists LLC, member KSRC/ISPF. Advisory services offered through Norwell Investment Advisers LLC.<br>
      Norwell entities are under separate ownership from any other entity.
    </p>
    <div class="base-band"></div>
  </footer>
</main>
</body>
</html>
```